property investment and development company needs a website

we need a website that looks professional and portrays trust for people looking to us to buy their house or investors looking to invest or joint venture with us.
We are based in the west midlands in the UK.
we deal mainly with residential housing, house to flats conversions, HMO's (houses in multiple ocupancy).
we require the website as a first point of contact with potential sellers, renters and investors so links or contact details that are easy to access or see would be good.
I have had logos designed by a brisk easel member and these can be used as guidance for the colour and style of the site.
Target Market(s)
joint venture investment partners, people looking to sell their house, people looking to rent from us.
Coding
Coded - Design and coding required
Number of Pages Required
3 page
Requirements
Must have
- project a professional appearance
- visable contact details

```html
<!DOCTYPE html>
<html lang="en">
<head>
<meta charset="utf-8">
<title>Alderby Estates</title>
<link href="https://fonts.googleapis.com/css2?family=Cinzel:wght@400;500&family=Lato:wght@400;700&family=Arimo:wght@400;700&display=swap" rel="stylesheet">
<style>
:root{
  --gold:#c9a468;
  --navy:#1f2736;
  --navy-deep:#222a39;
  --ink:#2b2b2b;
  --muted:#555;
  --field:#f1f2f4;
  --orange:#f7931e;
  --light:#ececec;
}
*{box-sizing:border-box;margin:0;padding:0}
html,body{width:1200px;height:3487px;overflow:hidden}
body{position:relative;background:#fff;font-family:"Lato",sans-serif;color:var(--ink)}
.abs{position:absolute}
.header{top:0;left:0;width:1200px;height:135px;background:#fff}
.brand{left:125px;top:50px;display:flex;align-items:center;gap:12px}
.brand-mark{width:14px;height:14px;background:var(--navy)}
.brand-name{font-family:"Lato",sans-serif;font-weight:700;color:var(--navy);font-size:28px;line-height:34px;white-space:nowrap}
.nav{right:74px;top:56px;display:flex;gap:40px;font-family:"Cinzel",serif;font-size:15px;letter-spacing:1px;color:#333}
.hero{top:135px;left:0;width:1200px;height:610px;background:linear-gradient(180deg,#2c3650 0%,#3e4a66 40%,#1c2436 70%,#4a5676 100%)}
.hero-cut{top:600px;left:0}
.hero-title{top:418px;left:0;width:1200px;text-align:center;font-family:"Lato",sans-serif;font-weight:700;color:#fff;font-size:56px}
.slide-btn{top:354px;width:150px;height:62px;background:rgba(80,86,100,.7);display:flex;align-items:center;justify-content:center}
.h2{font-family:"Cinzel",serif;font-weight:400;font-size:33px;letter-spacing:1px}
.body-text{font-size:12.5px;line-height:27.6px}
.btn{display:inline-block;background:var(--navy);color:#fff;font-weight:700;font-size:14px;padding:0 22px;height:37px;line-height:37px;clip-path:polygon(0 0,100% 0,88% 100%,0 100%)}
.photo{overflow:hidden}
.photo .frame{position:absolute;left:22px;top:22px;right:22px;bottom:22px;border:1px solid rgba(255,255,255,.7)}
.contact-panel{left:0;top:2252px;width:530px;height:723px;background:linear-gradient(180deg,#2d3440,#232a35)}
.arimo{font-family:"Arimo",sans-serif}
.info li{list-style:none;display:flex;align-items:flex-start;gap:18px;color:#fff;font-size:15px;line-height:27.6px}
.info svg{flex:0 0 14px;margin-top:7px}
.field{background:var(--field);font-family:"Arimo",sans-serif;font-weight:700;font-size:14px;color:#333;padding:14px 29px}
.footer{top:3140px;left:0;width:1200px;height:292px;background:var(--navy-deep)}
.input{background:#fff;border:1px solid #ccc;border-radius:2px;height:41px;font-family:"Arimo",sans-serif;font-size:14px;color:#555;padding:0 14px;line-height:41px}
.links li{list-style:none;color:#fff;font-family:"Arimo",sans-serif;font-size:15px;line-height:27.5px}
.links li::before{content:"›";margin-right:14px;font-weight:700}
.social{width:30px;height:30px;border-radius:50%;background:#4a5160}
.partner{height:28px;background:#c4c4c4;border-radius:3px}
</style>
</head>
<body>

<header class="abs header">
  <div class="abs brand"><span class="brand-mark"></span><div class="brand-name">Alderby Estates</div></div>
  <nav class="abs nav"><span>HOME</span><span>ABOUT US</span><span>INVEST</span><span>SELL</span><span>CONTACT US</span></nav>
</header>

<section class="abs hero" role="img" aria-label="Evening view of a riverside city skyline with clock tower and bridge"></section>
<svg class="abs hero-cut" width="1200" height="146" viewBox="0 0 1200 146"><polygon points="0,25 1200,146 0,146" fill="#fff"/></svg>
<div class="abs hero-title">Alderby Estates</div>
<div class="abs slide-btn" style="left:0"><svg width="16" height="24" viewBox="0 0 16 24"><path d="M13 2 3 12l10 10" stroke="#fff" stroke-width="4" fill="none"/></svg></div>
<div class="abs slide-btn" style="left:1048px"><svg width="16" height="24" viewBox="0 0 16 24"><path d="M3 2l10 10-10 10" stroke="#fff" stroke-width="4" fill="none"/></svg></div>

<section>
  <div class="abs photo" style="left:74px;top:804px;width:514px;height:387px;background:linear-gradient(135deg,#2a3a5a,#5a6d8e 50%,#a9b6c8)" role="img" aria-label="Business handshake over a city skyline"><div class="frame"></div></div>
  <h2 class="abs h2" style="left:636px;top:840px">INVEST</h2>
  <p class="abs body-text" style="left:636px;top:895px;width:488px">We have our own portfolio and we are active investors, so our finger is on the pulse and we are currently looking for residential development investments &amp; commercial to residential conversions in cities or regional centres showing strong growth.<br>Our experience in the industry enables us to make extremely quick and well-informed decisions. We follow the opportunities that are presented to us as well as sourcing opportunities ourselves. We are happy to work in partnership and within joint ventures and have a proven track record of establishing excellent relationships in these areas.</p>
  <span class="abs btn" style="left:636px;top:1116px">READ MORE</span>
</section>

<section>
  <svg class="abs" style="left:0;top:1247px" width="1200" height="610" viewBox="0 0 1200 610" role="img" aria-label="Dark overlay of a family at home"><polygon points="0,123 1200,0 1200,610 0,610" fill="#283042"/></svg>
  <h2 class="abs h2" style="left:74px;top:1438px;color:#fff">SELL</h2>
  <p class="abs body-text" style="left:74px;top:1493px;width:490px;color:#fff">We undertake the necessary market research to evaluate an option that works for all parties involved. We will help guide you to make an informed decision on how to gain the maximum realistic value.<br>For those looking to achieve a fast and professional sale to experienced investors, we provide an approach that has been proven to work for many others.</p>
  <span class="abs btn" style="left:74px;top:1648px;background:#3f4657;clip-path:none">READ MORE</span>
  <p class="abs" style="left:78px;top:1708px;color:#fff;font-size:14px">If you would like to discuss a property you are looking to sell, then please</p>
  <p class="abs" style="left:78px;top:1730px;color:var(--orange);font-size:24px;font-weight:700">contact us on 01632 960448</p>
  <div class="abs photo" style="left:614px;top:1396px;width:514px;height:386px;background:linear-gradient(160deg,#c9cfd6,#8a4b3a 40%,#6d3c30 70%,#6d7a4a)" role="img" aria-label="Agent showing a family a brick house"><div class="frame"></div></div>
</section>

<section>
  <h2 class="abs h2" style="left:0;top:1900px;width:1200px;text-align:center">ABOUT US</h2>
  <p class="abs body-text" style="left:200px;top:1956px;width:800px;text-align:center">We are a property development and investment company that have our own portfolio and we are active investors who pride ourselves in expanding our business organically.</p>
  <p class="abs body-text" style="left:200px;top:2039px;width:800px;text-align:center">We ensure that whatever your property needs are we deliver bespoke services for our clients. For investors, sellers, landlords and tenants we bring knowledge to your next property decision, allowing you to make an informed decision.</p>
  <span class="abs btn" style="left:520px;top:2117px;width:160px;text-align:center;clip-path:polygon(10% 0,100% 0,90% 100%,0 100%)">READ MORE</span>
</section>

<section>
  <div class="abs contact-panel" role="img" aria-label="Dark photo of a plant growing beside a stack of coins"></div>
  <h2 class="abs arimo" style="left:73px;top:2358px;color:#fff;font-size:26px;font-weight:700">CONTACT US</h2>
  <p class="abs arimo" style="left:78px;top:2412px;color:#fff;font-size:19px;font-weight:700">Alderby Estates &amp; Developments Ltd</p>
  <ul class="abs info arimo" style="left:82px;top:2446px">
    <li><svg width="14" height="16" viewBox="0 0 14 16"><path d="M7 0a6 6 0 0 0-6 6c0 4 6 10 6 10s6-6 6-10a6 6 0 0 0-6-6z" fill="#fff"/><circle cx="7" cy="6" r="2" fill="#2a313c"/></svg><span>12 Ashby Lane, Ledwell,<br>Worcestershire, WR0 1AA</span></li>
    <li><svg width="14" height="14" viewBox="0 0 14 14"><path d="M3 0l3 3-2 2c1 2 3 4 5 5l2-2 3 3-2 3C6 14 0 8 0 3z" fill="#fff"/></svg><span>01632 960448</span></li>
    <li><svg width="14" height="14" viewBox="0 0 14 14"><rect x="3" y="0" width="8" height="14" rx="1" fill="#fff"/></svg><span>07700 900109</span></li>
    <li><svg width="14" height="12" viewBox="0 0 14 12"><rect width="14" height="11" fill="#fff"/><path d="M0 0l7 6 7-6" stroke="#2a313c" fill="none"/></svg><span>info@alderbyestates.example</span></li>
    <li><svg width="14" height="14" viewBox="0 0 14 14"><rect x="2" y="0" width="10" height="14" fill="#fff"/><rect x="4" y="2" width="2" height="2" fill="#2a313c"/><rect x="8" y="2" width="2" height="2" fill="#2a313c"/><rect x="4" y="6" width="2" height="2" fill="#2a313c"/><rect x="8" y="6" width="2" height="2" fill="#2a313c"/></svg><span>Company No : 10293847</span></li>
  </ul>
  <div class="abs" style="left:74px;top:2662px;width:421px;height:240px;background:linear-gradient(135deg,#eef0f2,#e3e6ea)" role="img" aria-label="Street map showing the office location"></div>

  <h2 class="abs arimo" style="left:565px;top:2358px;font-size:26px;font-weight:700">GET IN TOUCH</h2>
  <p class="abs arimo" style="left:567px;top:2412px;width:520px;font-size:16px;line-height:27.6px;color:#333">Neque porro quisquam est qui dolorem ipsum quia dolor sit amet, consectetur, adipisci velit...</p>
  <div class="abs field" style="left:567px;top:2506px;width:272px;height:47px">NAME</div>
  <div class="abs field" style="left:853px;top:2506px;width:272px;height:47px">EMAIL</div>
  <div class="abs field" style="left:567px;top:2565px;width:558px;height:100px">MESSAGE</div>
  <div class="abs" style="left:572px;top:2685px;width:295px;height:77px;border:1px solid #d6d6d6;border-radius:3px;background:#f9f9f9">
    <div class="abs" style="left:16px;top:26px;width:26px;height:26px;border:2px solid #c1c1c1;background:#fff;border-radius:2px"></div>
    <span class="abs" style="left:56px;top:28px;font-size:15px;color:#333">I'm not a robot</span>
    <div class="abs" style="left:240px;top:18px;width:32px;height:32px;background:#c9ced6"></div>
  </div>
  <div class="abs arimo" style="left:578px;top:2794px;width:121px;height:41px;background:var(--navy);color:#fff;font-weight:700;font-size:14px;text-align:center;line-height:41px;border-radius:3px">SUBMIT</div>
</section>

<section>
  <svg class="abs" style="left:78px;top:3045px" width="12" height="20" viewBox="0 0 12 20"><path d="M10 2 2 10l8 8" stroke="#333" stroke-width="3" fill="none"/></svg>
  <div class="abs partner" style="left:142px;top:3041px;width:112px"></div>
  <div class="abs partner" style="left:352px;top:3034px;width:100px;height:40px"></div>
  <div class="abs partner" style="left:550px;top:3042px;width:107px;height:24px"></div>
  <div class="abs partner" style="left:750px;top:3035px;width:112px;height:40px"></div>
  <div class="abs partner" style="left:957px;top:3040px;width:102px;height:30px"></div>
  <svg class="abs" style="left:1112px;top:3045px" width="12" height="20" viewBox="0 0 12 20"><path d="M2 2l8 8-8 8" stroke="#333" stroke-width="3" fill="none"/></svg>
</section>

<footer class="abs footer">
  <h3 class="abs arimo" style="left:73px;top:68px;color:#fff;font-size:19px;font-weight:700">Sign up for our Newsletter</h3>
  <div class="abs input" style="left:73px;top:102px;width:197px">First name</div>
  <div class="abs input" style="left:278px;top:102px;width:197px">Last name</div>
  <div class="abs input" style="left:73px;top:159px;width:271px">Email Address</div>
  <div class="abs arimo" style="left:354px;top:159px;width:121px;height:41px;border:1px solid #fff;border-radius:2px;color:#fff;font-weight:700;font-size:14px;text-align:center;line-height:39px">SIGN UP</div>
  <h3 class="abs arimo" style="left:626px;top:68px;color:#fff;font-size:19px;font-weight:700">Quick Links</h3>
  <ul class="abs links" style="left:628px;top:96px"><li>Home</li><li>About Us</li><li>Invest</li><li>Sell</li><li>Contact us</li></ul>
  <h3 class="abs arimo" style="left:960px;top:68px;color:#fff;font-size:19px;font-weight:700">Follow Us</h3>
  <div class="abs social" style="left:962px;top:103px"></div>
  <div class="abs social" style="left:1007px;top:103px"></div>
  <div class="abs social" style="left:1052px;top:103px"></div>
  <div class="abs social" style="left:1094px;top:103px"></div>
  <div class="abs brand-name" style="right:74px;top:182px;font-size:22px;line-height:28px;color:#fff">Alderby Estates</div>
</footer>

<div class="abs" style="left:0;top:3432px;width:1200px;height:55px;background:var(--light)">
  <p class="abs" style="left:0;top:20px;width:1200px;text-align:center;font-size:11px;color:#333">© 2019 | www.alderbyestates.example</p>
  <span class="abs" style="right:28px;top:20px;font-size:11px;color:#555">M1</span>
</div>

</body>
</html>
```